MK Tallow Insurance - Aviation

We are wanting to have new business cards designed for our new aviation division. We currently have business cards for the other business (attached). We would like to use the same colors and have the logo somewhere on the business card along with a small, single engine airplane, maybe in the background but would like it to be different than the original and more focused on aviation. Also wondering if there is a way to do laser cut and make the business card in the shape of an airplane? Just some different ideas that make it stand out.

Target Market(s)

Pilots

Industry/Entity Type

Insurance

Contact Information for Business Card

We would like to use the same colors and have the logo somewhere on the business card along with a small, single engine airplane, maybe in the background but would like it to be different than the original and more focused on aviation. Also wondering if there is a way to do laser cut and make the business card in the shape of an airplane? Just some different ideas that make it stand out.

Requirements
Must have
• A small, single engine airplane

```html
<!DOCTYPE html>
<html lang="en">
<head>
<meta charset="utf-8">
<title>MK Tallow Insurance – Aviation Business Card</title>
<link href="https://fonts.googleapis.com/css2?family=Cinzel:wght@400;600&family=Montserrat:wght@400;500&display=swap" rel="stylesheet">
<style>
  :root {
    --backdrop: #c9c9cb;
    --card: #111112;
    --card-edge: #d0103a;
    --accent: #e0144a;
    --silver: #d8d8da;
    --text: #ececec;
    --rule: #8a8a8e;
    --sky-top: #2a2c30;
    --sky-bottom: #0f1012;
  }
  * { box-sizing: border-box; margin: 0; padding: 0; }
  html, body { width: 1200px; height: 800px; overflow: hidden; }
  body {
    background: var(--backdrop);
    font-family: "Montserrat", Arial, sans-serif;
    position: relative;
  }
  .card {
    position: absolute;
    top: 245px;
    width: 540px;
    height: 309px;
    background: var(--card);
    border-bottom: 3px solid var(--card-edge);
    box-shadow: 0 14px 30px rgba(0,0,0,0.25);
    overflow: hidden;
  }
  .card--back { left: 30px; }
  .card--front { left: 630px; }

  /* Back side */
  .brand-block {
    position: absolute;
    left: 40px; top: 70px;
    width: 200px;
    text-align: center;
  }
  .brand-mark {
    display: inline-flex;
    align-items: center;
    gap: 8px;
    font-family: "Cinzel", Georgia, serif;
    font-weight: 600;
    font-size: 17px;
    color: var(--accent);
    letter-spacing: 1px;
  }
  .brand-mark__dot {
    width: 12px; height: 12px; border-radius: 50%;
    background: var(--accent);
  }
  .agent-name {
    margin-top: 34px;
    font-family: "Cinzel", Georgia, serif;
    font-size: 24px;
    color: var(--accent);
    letter-spacing: 1px;
  }
  .agent-title {
    margin-top: 4px;
    font-size: 12px;
    color: var(--text);
  }
  .divider {
    position: absolute;
    height: 1px;
    background: linear-gradient(90deg, transparent, var(--silver), transparent);
  }
  .divider--top { left: 30px; top: 140px; width: 220px; }
  .divider--contact { left: 270px; top: 40px; width: 1px; height: 200px;
    background: linear-gradient(180deg, transparent, var(--silver), transparent); }
  .contact-list {
    position: absolute;
    left: 292px; top: 62px;
    list-style: none;
    font-size: 12.5px;
    color: var(--text);
    line-height: 1.45;
  }
  .contact-list li { display: flex; gap: 10px; align-items: flex-start; margin-bottom: 4px; }
  .contact-list svg { flex: none; margin-top: 3px; }
  .website {
    position: absolute;
    left: 0; right: 0; bottom: 34px;
    text-align: center;
    font-size: 12px;
    letter-spacing: 6px;
    color: var(--text);
  }
  .divider--bottom { left: 100px; bottom: 64px; width: 340px; }

  /* Front side */
  .aircraft-photo {
    position: absolute;
    left: 20px; top: 20px;
    width: 330px; height: 200px;
    background: radial-gradient(ellipse at 55% 50%, #c9ccd2 0%, #7f8794 30%, var(--sky-top) 60%, var(--sky-bottom) 100%);
    border-radius: 4px;
  }
  .front-brand {
    position: absolute;
    right: 30px; bottom: 48px;
    text-align: right;
  }
  .front-brand__rule {
    width: 230px; height: 1px; margin-left: auto; margin-bottom: 14px;
    background: linear-gradient(90deg, transparent, var(--silver));
  }
  .front-brand__name {
    font-family: "Cinzel", Georgia, serif;
    font-size: 27px;
    color: var(--silver);
    letter-spacing: 1px;
  }
</style>
</head>
<body>

<section class="card card--back" aria-label="Business card back">
  <div class="brand-block">
    <div class="brand-mark"><span class="brand-mark__dot"></span>MK Tallow Insurance</div>
    <div class="agent-name">Dana Whitfield</div>
    <div class="agent-title">Principal Agent</div>
  </div>
  <div class="divider divider--top"></div>
  <div class="divider divider--contact"></div>

  <ul class="contact-list">
    <li>
      <svg width="10" height="13" viewBox="0 0 10 13"><path d="M5 0a5 5 0 0 1 5 5c0 3.5-5 8-5 8S0 8.5 0 5a5 5 0 0 1 5-5z" fill="var(--accent)"/><circle cx="5" cy="5" r="2" fill="var(--card)"/></svg>
      <span>418 Linden Parkway<br>Alder, Texas 75010</span>
    </li>
    <li>
      <svg width="10" height="12" viewBox="0 0 10 12"><path d="M2 0l2 3-1 1.5c.8 1.6 1.8 2.6 3.4 3.4L8 7l2 2-1.5 2.5C4 11 0 6 0 1.5z" fill="var(--accent)"/></svg>
      <span>555-204-7716</span>
    </li>
    <li>
      <svg width="10" height="12" viewBox="0 0 10 12"><rect x="0.75" y="0.75" width="8.5" height="10.5" rx="1" fill="none" stroke="var(--accent)" stroke-width="1.5"/></svg>
      <span>555 318 2290</span>
    </li>
    <li>
      <svg width="11" height="9" viewBox="0 0 11 9"><rect width="11" height="9" rx="1" fill="var(--accent)"/><path d="M0.5 1l5 4 5-4" fill="none" stroke="var(--card)" stroke-width="1.2"/></svg>
      <span>dana@mktins.com</span>
    </li>
  </ul>

  <div class="divider divider--bottom"></div>
  <div class="website">WWW.MKTINS.COM</div>
</section>

<section class="card card--front" aria-label="Business card front">
  <div class="aircraft-photo" role="img" aria-label="Photograph of a white passenger jet with a blue tail climbing after takeoff"></div>
  <div class="front-brand">
    <div class="front-brand__rule"></div>
    <div class="front-brand__name">MK TALLOW INSURANCE</div>
  </div>
</section>

</body>
</html>
```